Post Card Invitation to Wedding Rehearsal Dinner and After Party

This post card should serve as invitations for two events in the wedding weekend for two San Francisco grooms, Derek and Leon.
Each side of the card should have distinct looks and information but tied together with “Before” on the front and “After” on the back.
POST CARD FRONT
Required text:
BEFORE
Derek and Leon’s Wedding: Rehearsal Dinner
Friday, May 22, 2015
5:30 PM
Larkfield Kitchen Yard
615 Fenwick Street @ Marlow
San Francisco, CA
Please also convey the following information without necessarily quoting directly: This rehearsal dinner will be held in a private enclosed space in the food truck park. We we will serve beer and wine in our space and provide tickets to purchase food from any of the trucks in the park. Dress is casual.
Look and feel of the card should have a modern, “hipster” feel to it. If you search Google images for “Hipster design” or “hipster infographic” you should get a sense of the overall design and colors. The website for the venue is http://larkfieldkitchenyard.com/ for reference but please DO NOT use any images or logos from the site.
----------------------
POST CARD REVERSE
Required Text:
AFTER
Derek and Leon’s Wedding: After Party
Saturday, May 23, 2015
7:30 PM
Harbor Crest Sailing Club
47 Pelling Road
San Francisco, CA
Please also convey the following information without necessarily quoting directly: Black-tie optional. Dancing, snacks and dessert and cocktails with panoramic views of the San Francisco Bay and Golden Gate Bridge.
This should have a much different look and feel from the front of the card. It should convey an elegant black-tie affair. If you search Google images for “black tie after party invitation” you should get some examples of an overall feel that I am aiming for. The website for the venue is www.hcsailclub.com but DO NOT use any of the images or logos from the site.
Industry/Entity Type
Wedding
Look and feel
Each slider illustrates characteristics of the customer's brand and the style your logo design should communicate.

```html
<!DOCTYPE html>
<html lang="en">
<head>
<meta charset="utf-8">
<title>Derek and Leon’s Wedding: After Party</title>
<link rel="stylesheet" href="https://fonts.googleapis.com/css2?family=Kaushan+Script&family=Arimo:wght@400;700&family=Roboto+Condensed:wght@400&display=swap">
<style>
  :root {
    --ink: #000000;
    --paper: #ffffff;
    --frame: #8c8c6c;
    --rule: #d4d4d4;
  }
  html, body {
    margin: 0;
    padding: 0;
    width: 1200px;
    height: 800px;
    overflow: hidden;
    background: var(--ink);
  }
  .postcard {
    position: relative;
    width: 1200px;
    height: 800px;
    background: var(--ink);
  }
  .card-face {
    position: absolute;
    left: 34px;
    top: 36px;
    width: 1124px;
    height: 720px;
    background: var(--paper);
    border: 4px solid var(--frame);
    border-radius: 28px;
    overflow: hidden;
  }
  .figure-art {
    position: absolute;
    left: 0;
    top: 0;
    width: 286px;
    height: 100%;
    background: linear-gradient(90deg, #0a0a0a 0%, #000 60%, #111 100%);
  }
  .event-word,
  .event-title {
    position: absolute;
    left: 0;
    width: 1124px;
    text-align: center;
    font-family: "Kaushan Script", cursive;
    color: var(--paper);
    mix-blend-mode: difference;
    margin: 0;
    white-space: nowrap;
  }
  .event-word {
    top: 30px;
    font-size: 46px;
    line-height: 1.2;
  }
  .event-title {
    top: 108px;
    font-size: 40px;
    line-height: 1.2;
    padding-left: 4px;
    box-sizing: border-box;
  }
  .event-date {
    position: absolute;
    left: 357px;
    top: 178px;
    margin: 0;
    font-family: "Arimo", Arial, sans-serif;
    font-weight: 700;
    font-size: 32px;
    color: var(--ink);
  }
  .event-venue {
    position: absolute;
    left: 306px;
    top: 230px;
    margin: 0;
    font-family: "Arimo", Arial, sans-serif;
    font-size: 16px;
    color: var(--ink);
    white-space: pre;
  }
  .event-details {
    position: absolute;
    left: 290px;
    top: 266px;
    width: 830px;
    margin: 0;
    text-align: center;
    font-family: "Roboto Condensed", "Arial Narrow", sans-serif;
    font-size: 23px;
    line-height: 35px;
    color: var(--ink);
  }
  .address-lines {
    position: absolute;
    left: 770px;
    top: 478px;
  }
</style>
</head>
<body>
  <main class="postcard">
    <section class="card-face">
      <div class="figure-art" role="img" aria-label="Black silhouette of a man in a tuxedo with white shirt cuffs, standing at the left edge"></div>

      <h2 class="event-word">After</h2>
      <h1 class="event-title">Derek and Leon’s Wedding: After Party</h1>
      <p class="event-date">Saturday, May 23, 2015</p>
      <p class="event-venue">7:30 PM Harbor Crest Sailing Club  47 Pelling Road,  San Francisco, CA</p>
      <p class="event-details">Black-tie optional. Dancing, snacks and dessert and cocktails with panoramic<br>views of the San Francisco Bay and Golden Gate Bridge.</p>

      <svg class="address-lines" width="340" height="60" viewBox="0 0 340 60" aria-hidden="true">
        <line x1="0" y1="3" x2="334" y2="3" stroke="var(--rule)" stroke-width="1.5" stroke-dasharray="5 3"/>
        <line x1="0" y1="53" x2="334" y2="53" stroke="var(--rule)" stroke-width="1.5" stroke-dasharray="5 3"/>
      </svg>
    </section>
  </main>
</body>
</html>
```